Marisol transparent business card

I would like to have a transparent business card created.
A simple yet classy card with
Website www.MarisolPennywhite.com
Phone # 555-417-2936
I would like my full photo on the card as well as my logo.

Target Market(s)

The business card will be printed on transparent card stock.
Www.MarisolPennywhite.com
Phone 555-417-2936
I would like my pic on the card and my logo
Author, Speaker, & Wealth architect

Industry/Entity Type

Business

Contact Information for Business Card

Www.MarisolPennywhite.com
Phone 555-417-2936

Font styles to use
Serif
Decorative
Script

Requirements
Must have
• The business card will be printed on transparent card stock.
• Www.MarisolPennywhite.com
• Phone 555-417-2936
• I would like my pic on the card and my logo
• Author, Speaker, & Wealth architect
Nice to have
• If I could have the tattoo on my pic blurred out or airbrushed over

```html
<!DOCTYPE html>
<html lang="en">
<head>
<meta charset="utf-8">
<title>Marisol Pennywhite – Business Card</title>
<link href="https://fonts.googleapis.com/css2?family=Lato:wght@400;700&display=swap" rel="stylesheet">
<style>
  :root {
    --stage: #e6e6e6;
    --card: #fbf1ed;
    --gold: #d6a936;
    --gold-light: #e8c35a;
    --ink: #1c1a1a;
    --band: #2b2224;
    --band-text: #d9d4d2;
    --photo-dark: #2a1d1a;
    --photo-mid: #6e4a3a;
    --photo-light: #c9a491;
  }
  * { box-sizing: border-box; margin: 0; padding: 0; }
  html, body { width: 1200px; height: 566px; overflow: hidden; }
  body {
    background: var(--stage);
    font-family: 'Lato', sans-serif;
    position: relative;
  }
  .business-card {
    position: absolute;
    left: 180px; top: 43px;
    width: 840px; height: 480px;
    background: var(--card);
    overflow: hidden;
    box-shadow: 0 6px 18px rgba(0,0,0,0.18);
  }
  .card-art { position: absolute; inset: 0; }
  .brand {
    position: absolute; left: 48px; top: 30px;
    display: flex; flex-direction: column; align-items: flex-start;
  }
  .brand-mark {
    width: 52px; height: 52px; border-radius: 50%;
    background: var(--gold); margin-left: 70px;
  }
  .brand-name {
    margin-top: 6px; font-size: 25px; font-weight: 400;
    color: var(--gold); letter-spacing: 0.5px;
  }
  .brand-tagline {
    margin-top: 2px; font-size: 8px; letter-spacing: 0.8px;
    color: var(--ink);
  }
  .holder { position: absolute; left: 70px; top: 160px; }
  .holder-name { font-size: 38px; font-weight: 700; color: var(--gold); line-height: 1; }
  .holder-title { font-size: 20px; color: var(--ink); margin-top: 4px; }
  .contact-list {
    position: absolute; left: 78px; top: 234px;
    list-style: none; font-size: 22px; color: var(--ink);
  }
  .contact-item { display: flex; align-items: center; gap: 14px; height: 32px; }
  .contact-icon { width: 20px; height: 20px; flex: none; }
  .role-line {
    position: absolute; left: 46px; bottom: 28px;
    font-size: 23px; letter-spacing: 1.5px; color: var(--band-text);
  }
</style>
</head>
<body>
  <div class="business-card">
    <svg class="card-art" width="840" height="480" viewBox="0 0 840 480">
      <defs>
        <linearGradient id="portraitTone" x1="0" y1="0" x2="0" y2="1">
          <stop offset="0" stop-color="var(--photo-mid)"/>
          <stop offset="0.45" stop-color="var(--photo-light)"/>
          <stop offset="1" stop-color="var(--photo-dark)"/>
        </linearGradient>
      </defs>
      <rect x="540" y="10" width="290" height="360" rx="120" fill="url(#portraitTone)"
            role="img" aria-label="Portrait photo of Marisol Pennywhite"/>
      <path d="M0 404 Q 420 402 840 292 L840 480 L0 480 Z" fill="var(--band)"/>
      <path d="M0 392 Q 420 384 840 268 L840 294 Q 420 404 0 406 Z" fill="var(--gold-light)"/>
    </svg>

    <div class="brand">
      <div class="brand-mark"></div>
      <div class="brand-name">Marisol Pennywhite</div>
      <div class="brand-tagline">LIVE WITH INTENT, BUILD YOUR LEGACY</div>
    </div>

    <div class="holder">
      <div class="holder-name">Your Name</div>
      <div class="holder-title">President</div>
    </div>

    <ul class="contact-list">
      <li class="contact-item">
        <svg class="contact-icon" viewBox="0 0 20 20"><path d="M3 8 Q10 2 17 8 L15 10 L12 8 L8 8 L5 10 Z M5 11 H15 L16 17 H4 Z" fill="var(--gold)"/></svg>
        <span>555-417-2936</span>
      </li>
      <li class="contact-item">
        <svg class="contact-icon" viewBox="0 0 20 20"><rect x="2" y="4" width="16" height="12" fill="var(--gold)"/><path d="M2 4 L10 11 L18 4" fill="none" stroke="var(--card)" stroke-width="1.5"/></svg>
        <span>@MarisolPennywhite.com</span>
      </li>
      <li class="contact-item">
        <svg class="contact-icon" viewBox="0 0 20 20"><rect x="3" y="4" width="14" height="10" fill="none" stroke="var(--gold)" stroke-width="2"/><rect x="7" y="15" width="6" height="2" fill="var(--gold)"/></svg>
        <span>Www.MarisolPennywhite.com</span>
      </li>
    </ul>

    <div class="role-line">Author, Speaker, &amp; Wealth architect</div>
  </div>
</body>
</html>
```